Vaultrix Web Site

Hi Designers. Our web site at www.vaultrix.net.au needs a new look.

We do:

- off-site backup, every day, for vital data
- data recovery from crashed disks

We have an existing logo

Our colour is blue. Our image is about Trust and Competence

We are in Perth, Western Australia. Our photographs are local images.

We've been in business for fifteen years.

We have a second URL too: www.keep-our-records.com.au

Both URLs go to the same web site.

Would you like to take on this project?

Target Market(s)

Target market is small to medium business, with between 5 and 100 staff. Customers are mainly in Australia but can be anywhere. There are other providers who are cheaper- our point of difference is that we are highly professional and have been in the business for 15 years. personal attention is important to us- we promise Extreme Service.

Industry/Entity Type

Data Recovery

Requirements
Must have
• Our image is about Trust and Competence. Existing text from our web site can be used.
Should not have
• No moving Flash, no Flash intro

```html
<!DOCTYPE html>
<html lang="en">
<head>
<meta charset="utf-8">
<title>Vaultrix – Off-site Backup and Data Recovery</title>
<link href="https://fonts.googleapis.com/css2?family=Arimo:wght@400;700&family=Source+Sans+3:wght@400;600&display=swap" rel="stylesheet">
<style>
:root{
  --page:#f6f6f6;
  --ink:#222;
  --navy:#0f3a66;
  --heading-blue:#0e3d73;
  --green:#5a9a0a;
  --green-dark:#6f9222;
  --nav-bg:#3a3a3a;
  --footer-top:#3c6690;
  --footer-bottom:#0d2d52;
  --bullet:#b3121a;
  --rule:#b9b9b9;
  --accent-red:#a3141b;
}
*{box-sizing:border-box;margin:0;padding:0}
html,body{width:1200px;height:1100px;overflow:hidden}
body{
  background:linear-gradient(to bottom,var(--page) 0,var(--page) 931px,#1f4a74 931px,var(--footer-top) 935px,var(--footer-bottom) 1100px);
  font-family:"Arimo",Arial,sans-serif;color:var(--ink);position:relative;
}
.site{position:absolute;left:150px;top:18px;width:900px;height:967px;background:#fff;
  box-shadow:0 0 6px rgba(0,0,0,.25);border-bottom:3px solid var(--accent-red);border-radius:0 0 4px 4px}
.masthead{position:relative;height:113px;background:linear-gradient(to bottom,#e2e2e2,#cfcfcf 70%,#dcdcdc)}
.brand{position:absolute;left:22px;top:30px;display:flex;align-items:center;gap:10px;
  font-family:"Source Sans 3",sans-serif;font-weight:600;font-size:30px;color:var(--navy)}
.brand-mark{width:26px;height:26px;border-radius:50%;background:var(--navy)}
.support{position:absolute;left:648px;top:34px;font-size:13.5px;line-height:17px;color:#000}
.support .big{font-size:16.5px;line-height:19px}
.main-nav{height:33px;background:var(--nav-bg);display:flex;padding-left:22px;align-items:flex-end}
.main-nav a{color:#fff;text-decoration:none;font-size:13.5px;height:29px;line-height:31px;padding:0 14px;margin-right:1px}
.main-nav a.active{background:var(--green-dark);color:#000;padding:0 16px}
.hero{position:relative;height:300px;overflow:hidden;
  background:linear-gradient(100deg,#2a5bd0 0%,#4e8cf0 45%,#2d6ae6 75%,#5b8fe8 100%)}
.hero-photo{position:absolute;left:0;top:0;width:470px;height:300px;
  background:radial-gradient(ellipse at 55% 45%,#7fa8f2 0%,#3a67cf 45%,#0d1f55 100%)}
.hero-copy{position:absolute;left:487px;top:46px;font-family:"Source Sans 3",sans-serif;color:#05070d;
  font-size:29px;line-height:28px;letter-spacing:-.5px}
.hero-copy p+p{margin-top:18px}
.learn-btn{position:absolute;left:487px;top:194px;width:204px;height:46px;border-radius:4px;
  background:linear-gradient(#8bb83a,#5a8a18);color:#fff;font-family:"Source Sans 3",sans-serif;font-size:29px;
  line-height:48px;text-align:center;box-shadow:0 3px 6px rgba(0,0,0,.3)}
.hero-curve{position:absolute;left:0;bottom:0}
.columns{position:relative;height:330px}
.col{position:absolute;top:0;width:262px}
.col.about{left:18px}
.col.services{left:300px;width:300px;height:330px;padding:0 20px;
  background:linear-gradient(to bottom,#e8e8e8,#f6f6f6 50%,#fff)}
.col.why{left:622px}
.col h2{font-family:"Source Sans 3",sans-serif;font-weight:400;font-size:23px;color:var(--heading-blue);
  padding-top:21px;height:54px;border-bottom:1px solid var(--rule);position:relative;margin-bottom:9px}
.col h2::after{content:"";position:absolute;left:0;bottom:2px;width:215px;border-bottom:1px solid var(--rule)}
.col.services h2{color:#111}
.col.services h2.second{padding-top:17px;height:50px}
.col p{font-size:11.7px;line-height:18.75px}
.col a{color:var(--green);text-decoration:none}
.why ul{list-style:none;font-size:11.7px;line-height:16.8px}
.why li{position:relative;padding-left:20px;margin-bottom:11.3px}
.why li::before{content:"";position:absolute;left:9px;top:6px;width:4px;height:4px;border-radius:50%;background:var(--bullet)}
.lower{position:absolute;left:0;top:773px;width:900px;height:191px;background:linear-gradient(#efefef,#fff 40%)}
.box{position:absolute;top:28px;width:259px;height:136px;border:1px solid #d8d8d8;border-radius:3px;
  background:linear-gradient(#fff,#f1f1f1)}
.box h3{font-family:"Source Sans 3",sans-serif;font-weight:400;font-size:18px;height:31px;line-height:31px;
  padding-left:9px;border-bottom:1px solid #dcdcdc;color:#222;background:linear-gradient(#f8f8f8,#ececec)}
.box.testimonial{left:18px}
.box.clients{left:321px}
.box.cta{left:624px}
.box.cta h3{background:linear-gradient(#1c4c80,var(--navy));color:#fff;border-bottom:none}
.testimonial blockquote{padding:17px 11px 0;font-size:11.5px;line-height:17px}
.testimonial .who{margin-top:6px}
.testimonial .who b{display:block}
.client-strip{display:flex;align-items:center;justify-content:center;gap:12px;padding-top:14px}
.client-logo{width:168px;height:80px;border:1px solid #cfcfcf;border-radius:3px;background:#fff;
  display:flex;align-items:center;justify-content:center;font-family:"Source Sans 3",sans-serif;
  font-weight:600;font-size:19px;color:#1f5aa8}
.cta-body{text-align:center;padding-top:18px;font-size:17px;line-height:23px;color:#333}
.cta-body .cta-title{color:var(--green);font-weight:700;font-size:16.5px;margin-bottom:2px}
.cta-body b{display:block}
.site-footer{position:absolute;left:0;top:1026px;width:1200px;text-align:center}
.site-footer nav a{color:#fff;text-decoration:none;font-size:11.7px;margin:0 11px}
.site-footer small{display:block;margin-top:16px;font-size:10.5px;color:#8ba8c8}
</style>
</head>
<body>
<div class="site">
  <header class="masthead">
    <div class="brand"><span class="brand-mark"></span>Vaultrix</div>
    <div class="support">For More Information and Support<div class="big">Call: +61 8 9000 4127<br>Email: service@vaultrix.net.au</div></div>
  </header>
  <nav class="main-nav">
    <a class="active">HOME</a><a>REMOTE BACKUP</a><a>EMERGENCY RECOVERY</a><a>TESTIMONIALS</a><a>OUR CLIENTS</a><a>ABOUT US</a><a>CONTACT US</a>
  </nav>
  <section class="hero">
    <div class="hero-photo" role="img" aria-label="Close-up photograph of an open hard disk platter and read arm in blue light"></div>
    <div class="hero-copy"><p>OFF-SITE BACKUP, EVERY DAY,<br>FOR VITAL DATA.</p><p>DATA RECOVERY FROM<br>CRASHED DISKS.</p></div>
    <div class="learn-btn">LEARN MORE</div>
    <svg class="hero-curve" width="900" height="300" viewBox="0 0 900 300"><path d="M0 247 Q430 322 900 244 L900 300 L0 300 Z" fill="#fff"/></svg>
  </section>
  <section class="columns">
    <div class="col about">
      <h2>About Vaultrix...</h2>
      <p>Lorem Ipsum is simply dummy text of the printing and typesetting industry. Lorem Ipsum has been the industry's standard dummy text ever since the 1500s, when an unknown printer took a galley of type and scrambled it to make a type specimen book. It has survived not only five centuries, but also the leap into electronic typesetting, remaining essentially unchanged. It was popularised in the 1960s with the release of Stencilon sheets containing Lorem Ipsum passages, and more recently with desktop publishing software like Quillset Publisher including versions of Lorem Ipsum. <a>Learn more...</a></p>
    </div>
    <div class="col services">
      <h2>Remote Backup...</h2>
      <p>Lorem Ipsum is simply dummy text of the printing and typesetting industry. Lorem Ipsum has been the industry's standard dummy text ever since the 1500s, when an unknown printer took a galley of type. <a>Learn more...</a></p>
      <h2 class="second">Emergency Recovery...</h2>
      <p>Lorem Ipsum is simply dummy text of the printing and typesetting industry. Lorem Ipsum has been the industry's standard dummy text ever since the 1500s, when an unknown printer took a galley of type. <a>Learn more...</a></p>
    </div>
    <div class="col why">
      <h2>Why Vaultrix...</h2>
      <ul>
        <li>Safe &amp; Secure.</li>
        <li>Reliable backup is a vital part of risk management.</li>
        <li>We keep your business records safe, always.</li>
        <li>Database, Customer List, Financials, Contracts.</li>
        <li>Every hard disk fails one day.</li>
        <li>We backup these valuable assets.</li>
        <li>Critical data backup off-site, every night.</li>
        <li>Located in Perth, Western Australia- the safest place on Earth.</li>
      </ul>
    </div>
  </section>
  <section class="lower">
    <div class="box testimonial">
      <h3>Testimonails</h3>
      <blockquote>Thank you for all your wonderful support - what would we do without you?
        <div class="who"><b>Megan Hollis,</b>Riverside Family Services of WA</div></blockquote>
    </div>
    <div class="box clients">
      <h3>Clients</h3>
      <div class="client-strip">
        <svg width="18" height="20" viewBox="0 0 18 20"><path d="M14 2 L5 10 L14 18" fill="none" stroke="#333" stroke-width="4"/></svg>
        <div class="client-logo">Harbourline Marine</div>
        <svg width="18" height="20" viewBox="0 0 18 20"><path d="M4 2 L13 10 L4 18" fill="none" stroke="#333" stroke-width="4"/></svg>
      </div>
    </div>
    <div class="box cta">
      <h3>Backup My Files Now!</h3>
      <div class="cta-body"><div class="cta-title">CONTACT US</div>To keep your data safe.<b>Today and every day.</b></div>
    </div>
  </section>
</div>
<footer class="site-footer">
  <nav><a>Home</a><a>Remote Backup</a><a>Emergency Recovery</a><a>Testimonials</a><a>Our Clients</a><a>About Us</a><a>Contact Us</a></nav>
  <small>© 2011 - Vaultrix Computer Services | All Rights Reserved.</small>
</footer>
</body>
</html>
```